Lotvantage.com Webpage Design

Design Brief for lotvantage.com (Copy of Brief also in attached Word file)

Name of Website- lotvantage.com (existing logo and look & feel of website to be changed)

Logo - Finalised. The logo files are attached with the brief as “logo.jpeg”. The “Blue- Grey” version of the logo is for use on lighter backgrounds and the “Orange-White” version of the logo is for use on darker backgrounds. (A full Black version of the logo is also attached). Both versions may be used in different parts of the website. All attached files are in .png format.
Status - The website in functional and is undergoing user trials. However, we want to improve the look & feel of the website so at it seems
a. cotemporary,
b. Easy to Navigate
c. professional and
d. Vibrant.

Please visit ‘lotvantage.com’ to check out the website and its functionalities – please use it only as a reference for the features & functions to be provided, however the designer should use a ‘Free Hand’ in designing the composition of various parts of the webpage without getting too influenced by the existing design

Objective of the Website ‘lotvantage.com –
a. It is a portal focussed on listing of ‘Retail’ specific real-estate properties by developers, owners and realty brokers. The properties shall listed under the following four categories-
i. Retail Malls
ii. Shopping Complexes
iii. High-street shops
iv. Retail Warehouses
*refer lotvantage.com for better clarity

b. The abovementioned properties shall be listed either for ‘Sale’ or ‘rent\lease’ or both

c. Users shall visit the site in case they wish to acquire a retail \ shop space either on ‘sale’ or ‘rent’. These Users would be able to specify the ‘Search Criteria’ through the tool-bars provided on the website – the ‘Search Criteria’ shall comprise of ‘Type of space category’, ‘City’, ‘Locality’, transaction type ie ‘Rent \ Sale’ and ‘Area Range’

d. The main revenue model for the website shall be listing fee ( or advertising charges ) payable by those listing their properties on the website.

Three Main Pages of Website (lotvantage.com) that need to be designed -
a. Main Home Page (visit the web link - http://lotvantage.com/ ) - The main home page has the “Search Toolbar” for specifying of Search Criteria by the User. It shall also have the following features & functions-
i. Main Advertising Banner
ii. Featured Projects
iii. New Launches
iv. Toolbar with buttons – ‘Advertise with Us’, ‘Listings Alert’, ‘Lot Mavens’, ‘Advertiser Login’

b. Property Listings Page (visit the web link - http://lotvantage.com/gurgaon-in-india ) - The List of property options that match the Criteria specified by the ‘User’ get displayed on this page.

c. Property Detail Page - When the ‘User’ clicks on the “More….” Button on the ‘Property Listings Page’ (given in point b. above) the web page with the details of the property opens. (For Example – visit the web link - http://lotvantage.com/brevo-Shopping-Complex-brevo-quadrel-gurgaon-636 )

Note:- Please refer to attached ‘Shopping’ related images the designer may use them on the website to provide a look & feel of retail if required – either separately or rotate in a single window

Target Market(s)

Retailers & Investors looking for retail space, Real Estate Brokers, Developers

Industry/Entity Type

Advertising

Number of Pages Required

3 page

Requirements
Must have
• Refer to existing site lotvantage.com -- all the existing functionalities are a must have.
Nice to have
• The Designer may use the retail related images on the website if required for making it more vibrant. Refer attached images Shopping(1-6).jpg

```html
<!DOCTYPE html>
<html lang="en">
<head>
<meta charset="utf-8">
<title>Lotvantage.com – Retail Space Portal</title>
<link href="https://fonts.googleapis.com/css2?family=Open+Sans:wght@400;600;700&family=Roboto+Condensed:wght@300;400;700&display=swap" rel="stylesheet">
<style>
:root{
  --blue:#1f8fe5;
  --blue-dark:#1570c0;
  --ink:#333;
  --muted:#777;
  --bar:#3a3a3a;
  --bar-deep:#2a2a2a;
  --panel:#ececec;
  --line:#bcdcf5;
  --white:#fff;
}
*{box-sizing:border-box;margin:0;padding:0}
html,body{width:1200px;height:2911px;overflow:hidden}
body{position:relative;background:var(--white);font-family:"Open Sans",sans-serif;color:var(--ink);font-size:13px}
.abs{position:absolute}

/* top bar */
.topbar{left:0;top:0;width:1200px;height:58px;background:var(--bar)}
.location-select{left:26px;top:16px;width:207px;height:28px;background:var(--white);border-radius:2px;font-size:11px;color:var(--muted);padding:6px 10px;text-transform:uppercase}
.location-select span{position:absolute;right:0;top:0;width:26px;height:28px;background:var(--blue);color:#fff;text-align:center;line-height:28px;font-size:10px}
.nav-item{top:8px;color:#fff;font-family:"Roboto Condensed",sans-serif;font-size:12px;text-align:center;text-transform:uppercase;letter-spacing:.3px}
.nav-item svg{display:block;margin:0 auto 4px}
.nav-item u{text-decoration:none;border-bottom:2px solid var(--blue);padding-bottom:2px}
.login-box{left:1030px;top:0;width:170px;height:58px;background:var(--bar-deep);color:#fff;font-family:"Roboto Condensed",sans-serif;text-align:center;padding-top:8px}
.login-box b{display:block;font-size:15px;letter-spacing:.3px}
.login-box small{display:block;font-size:11px;margin-top:6px;color:#ccc}
.login-box small em{font-style:normal;color:#fff;font-weight:700}

/* brand */
.brand{display:flex;align-items:center;gap:10px}
.brand-dot{width:40px;height:40px;border-radius:50%;background:var(--blue);flex:none}
.brand-name{font-family:"Open Sans",sans-serif;font-weight:700;font-size:38px;color:#445;letter-spacing:-.5px;line-height:1}
.brand-tag{font-size:9px;color:var(--muted);text-transform:uppercase;letter-spacing:.6px;margin-top:4px;margin-left:50px}
.brand-light .brand-name{color:var(--white)}
.brand-light .brand-tag{color:#bbb}

/* hero */
.search-panel{left:0;top:58px;width:356px;height:615px;background:var(--white)}
.hero-brand{left:26px;top:136px}
.check{top:255px;font-size:12px;color:#555;display:flex;align-items:center;gap:8px;text-transform:uppercase}
.check i{width:16px;height:16px;border:1px solid #999;display:inline-block;position:relative}
.field{left:26px;width:298px;height:30px;border:1px solid #ccc;font-size:11px;color:#888;padding:7px 10px;text-transform:uppercase}
.field span{position:absolute;right:-1px;top:-1px;width:28px;height:30px;background:var(--blue);color:#fff;text-align:center;line-height:30px;font-size:10px}
.btn{background:var(--blue);color:#fff;text-transform:uppercase;text-align:center;font-family:"Roboto Condensed",sans-serif;font-weight:700}
.search-btn{left:97px;top:501px;width:153px;height:36px;line-height:36px;font-size:15px}
.hero-photo{left:356px;top:58px;width:844px;height:615px;background:linear-gradient(120deg,#c9d3dc 0%,#8fa4b8 40%,#d8dde2 70%,#6d7f92 100%)}
.hero-line{left:390px;color:#fff;font-family:"Roboto Condensed",sans-serif;font-size:40px;font-weight:300;text-transform:uppercase;background:rgba(20,30,40,.75);padding:0 12px;line-height:56px}
.hero-line b{font-weight:700}

/* sections */
.section-head{left:0;width:1200px;height:30px;display:flex;align-items:center;justify-content:center}
.section-head::before{content:"";flex:1;height:1px;background:var(--line)}
.section-head .rule{flex:1;height:1px;background:var(--line)}
.section-head h2{font-family:"Roboto Condensed",sans-serif;color:var(--blue);font-size:22px;font-weight:700;text-transform:uppercase;padding:0 16px}
.section-head .scope{font-family:"Roboto Condensed",sans-serif;color:#444;font-size:13px;text-transform:uppercase;padding-right:20px}
.grid{left:22px;width:1156px;display:grid;grid-template-columns:repeat(5,200px);column-gap:39px;row-gap:16px}
.card{height:243px;border:1px solid var(--line);background:#fff}
.card-img{height:113px;background:linear-gradient(160deg,#7f9fc0,#c5d2de 55%,#55708a)}
.card-city{height:22px;line-height:22px;background:var(--blue);color:#fff;text-align:center;font-family:"Roboto Condensed",sans-serif;font-weight:700;font-size:13px}
.card-body{padding:8px 12px 0}
.card-name{font-weight:700;font-size:11px;margin-bottom:3px}
.card-row{display:flex;align-items:center;gap:5px;font-size:10px;color:#666;margin-bottom:2px}
.card-btn{display:block;margin:8px auto 0;width:90px;height:22px;line-height:22px;font-size:10px}

/* mavens */
.maven{left:0;top:1935px;width:1200px;height:297px;background:var(--panel)}
.maven-art{left:32px;top:1973px;width:291px;height:243px;background:radial-gradient(circle at 50% 45%,#e7c9a8,#9bc3d9 55%,#d8dde2);border-radius:4px}
.block-title{font-family:"Roboto Condensed",sans-serif;color:var(--blue);font-size:26px;font-weight:400;text-transform:uppercase}
.block-text{font-size:12.5px;color:#555;line-height:17px}
.input{height:26px;border:1px solid var(--line);background:#fff;font-size:10px;color:#999;padding:6px 10px;text-transform:uppercase;display:flex;align-items:center;gap:6px}
.textarea{align-items:flex-start}

/* duo */
.duo-box{top:2239px;height:252px;background:#fff;border:1px solid #e2e2e2}
.editors-art{left:36px;top:2280px;width:124px;height:170px;border-radius:6px;background:linear-gradient(180deg,#5fb0ee 0%,#1f8fe5 60%,#8a8a8a 100%)}

/* footer */
.footer{left:0;top:2517px;width:1200px;height:323px;background:var(--bar)}
.footer-text{left:26px;top:2620px;width:310px;color:#ddd;font-size:12.5px;line-height:17px;text-align:justify}
.getintouch{left:480px;top:2530px;width:700px;height:34px;background:#2c2c2c;color:var(--blue);font-family:"Roboto Condensed",sans-serif;font-size:22px;text-align:center;line-height:34px;text-transform:uppercase}
.address{left:480px;top:2588px;color:#ddd;font-size:12.5px;line-height:17px}
.social{left:520px;top:2748px;display:flex;gap:9px}
.social i{width:24px;height:24px;border-radius:50%;background:#fff;display:block}
.input.on-dark{border-color:#fff}
.bottom-nav{left:0;top:2840px;width:1200px;height:46px;background:#4a4a4a;display:flex;justify-content:space-between;align-items:center;padding:0 16px;color:#fff;font-size:13.5px}
.copyright{left:0;top:2886px;width:1200px;height:25px;background:#2b2b2b;color:#bbb;font-size:10px;text-align:center;line-height:25px}
</style>
</head>
<body>

<!-- top bar -->
<div class="abs topbar"></div>
<div class="abs location-select">Select Location<span>▼</span></div>
<div class="abs nav-item" style="left:570px">
  <svg width="18" height="18" viewBox="0 0 18 18"><path d="M2 8 9 2l7 6v8H2z" fill="#fff"/></svg><u>List Your Property</u></div>
<div class="abs nav-item" style="left:772px">
  <svg width="18" height="18" viewBox="0 0 18 18"><circle cx="9" cy="6" r="4" fill="#fff"/><path d="M2 17c0-4 3-6 7-6s7 2 7 6z" fill="#fff"/></svg><u>Lot Mavens</u></div>
<div class="abs nav-item" style="left:912px">
  <svg width="18" height="18" viewBox="0 0 18 18"><path d="M9 2c3 0 5 2 5 5v5l2 2H2l2-2V7c0-3 2-5 5-5z" fill="#fff"/><circle cx="9" cy="16" r="1.6" fill="#fff"/></svg><u>Listing Alert</u></div>
<div class="abs login-box"><b>🔒 ADVERTISER LOGIN</b><small>NEW USER <em>SIGNUP</em></small></div>

<!-- hero -->
<div class="abs search-panel"></div>
<div class="abs hero-brand">
  <div class="brand"><span class="brand-dot"></span><span class="brand-name">Lotvantage</span></div>
  <div class="brand-tag">India's leading portal for retail space</div>
</div>
<div class="abs check" style="left:30px"><i style="border-color:var(--blue)"><svg width="14" height="14" viewBox="0 0 14 14"><path d="M2 7l3 3 7-7" stroke="#1f8fe5" stroke-width="2" fill="none"/></svg></i>For Sale</div>
<div class="abs check" style="left:205px"><i></i>For Rent</div>
<div class="abs field" style="top:307px">Property Type<span>▼</span></div>
<div class="abs field" style="top:356px">Select City<span>▼</span></div>
<div class="abs field" style="top:401px">Select Locality<span>▼</span></div>
<div class="abs field" style="top:450px">Enter Keywords</div>
<div class="abs btn search-btn">Search</div>

<div class="abs hero-photo" role="img" aria-label="Smiling businessman standing in a bright shopping mall aisle"></div>
<div class="abs hero-line" style="top:224px">Find the best <b>Retail Space</b></div>
<div class="abs hero-line" style="top:286px">That your business <b>deserves</b></div>

<!-- featured retail projects -->
<div class="abs section-head" style="top:713px"><h2>Featured Retail Projects</h2><span class="scope">Across India ▾</span><span class="rule"></span></div>

<div class="abs grid" style="top:776px">
  <div class="card"><div class="card-img" role="img" aria-label="Shopping complex exterior"></div><div class="card-city">GURGAON</div><div class="card-body"><div class="card-name">Kestrel Cosmopolitan</div><div class="card-row"><svg width="9" height="11" viewBox="0 0 9 11"><path d="M4.5 0A4 4 0 0 1 8.5 4c0 3-4 7-4 7S.5 7 .5 4a4 4 0 0 1 4-4z" fill="#888"/></svg>Sector-65, Noida</div><div class="card-row"><svg width="10" height="10" viewBox="0 0 10 10"><rect x="1" y="1" width="8" height="9" fill="#888"/></svg>Shopping Complex</div><div class="btn card-btn">View Details</div></div></div>
  <div class="card"><div class="card-img" role="img" aria-label="Shopping complex exterior"></div><div class="card-city">GURGAON</div><div class="card-body"><div class="card-name">Kestrel Cosmopolitan</div><div class="card-row"><svg width="9" height="11" viewBox="0 0 9 11"><path d="M4.5 0A4 4 0 0 1 8.5 4c0 3-4 7-4 7S.5 7 .5 4a4 4 0 0 1 4-4z" fill="#888"/></svg>Sector-65, Noida</div><div class="card-row"><svg width="10" height="10" viewBox="0 0 10 10"><rect x="1" y="1" width="8" height="9" fill="#888"/></svg>Shopping Complex</div><div class="btn card-btn">View Details</div></div></div>
  <div class="card"><div class="card-img" role="img" aria-label="Shopping complex exterior"></div><div class="card-city">GURGAON</div><div class="card-body"><div class="card-name">Kestrel Cosmopolitan</div><div class="card-row"><svg width="9" height="11" viewBox="0 0 9 11"><path d="M4.5 0A4 4 0 0 1 8.5 4c0 3-4 7-4 7S.5 7 .5 4a4 4 0 0 1 4-4z" fill="#888"/></svg>Sector-65, Noida</div><div class="card-row"><svg width="10" height="10" viewBox="0 0 10 10"><rect x="1" y="1" width="8" height="9" fill="#888"/></svg>Shopping Complex</div><div class="btn card-btn">View Details</div></div></div>
  <div class="card"><div class="card-img" role="img" aria-label="Shopping complex exterior"></div><div class="card-city">GURGAON</div><div class="card-body"><div class="card-name">Kestrel Cosmopolitan</div><div class="card-row"><svg width="9" height="11" viewBox="0 0 9 11"><path d="M4.5 0A4 4 0 0 1 8.5 4c0 3-4 7-4 7S.5 7 .5 4a4 4 0 0 1 4-4z" fill="#888"/></svg>Sector-65, Noida</div><div class="card-row"><svg width="10" height="10" viewBox="0 0 10 10"><rect x="1" y="1" width="8" height="9" fill="#888"/></svg>Shopping Complex</div><div class="btn card-btn">View Details</div></div></div>
  <div class="card"><div class="card-img" role="img" aria-label="Shopping complex exterior"></div><div class="card-city">GURGAON</div><div class="card-body"><div class="card-name">Kestrel Cosmopolitan</div><div class="card-row"><svg width="9" height="11" viewBox="0 0 9 11"><path d="M4.5 0A4 4 0 0 1 8.5 4c0 3-4 7-4 7S.5 7 .5 4a4 4 0 0 1 4-4z" fill="#888"/></svg>Sector-65, Noida</div><div class="card-row"><svg width="10" height="10" viewBox="0 0 10 10"><rect x="1" y="1" width="8" height="9" fill="#888"/></svg>Shopping Complex</div><div class="btn card-btn">View Details</div></div></div>
  <div class="card"><div class="card-img" role="img" aria-label="Shopping complex exterior"></div><div class="card-city">GURGAON</div><div class="card-body"><div class="card-name">Kestrel Cosmopolitan</div><div class="card-row"><svg width="9" height="11" viewBox="0 0 9 11"><path d="M4.5 0A4 4 0 0 1 8.5 4c0 3-4 7-4 7S.5 7 .5 4a4 4 0 0 1 4-4z" fill="#888"/></svg>Sector-65, Noida</div><div class="card-row"><svg width="10" height="10" viewBox="0 0 10 10"><rect x="1" y="1" width="8" height="9" fill="#888"/></svg>Shopping Complex</div><div class="btn card-btn">View Details</div></div></div>
  <div class="card"><div class="card-img" role="img" aria-label="Shopping complex exterior"></div><div class="card-city">GURGAON</div><div class="card-body"><div class="card-name">Kestrel Cosmopolitan</div><div class="card-row"><svg width="9" height="11" viewBox="0 0 9 11"><path d="M4.5 0A4 4 0 0 1 8.5 4c0 3-4 7-4 7S.5 7 .5 4a4 4 0 0 1 4-4z" fill="#888"/></svg>Sector-65, Noida</div><div class="card-row"><svg width="10" height="10" viewBox="0 0 10 10"><rect x="1" y="1" width="8" height="9" fill="#888"/></svg>Shopping Complex</div><div class="btn card-btn">View Details</div></div></div>
  <div class="card"><div class="card-img" role="img" aria-label="Shopping complex exterior"></div><div class="card-city">GURGAON</div><div class="card-body"><div class="card-name">Kestrel Cosmopolitan</div><div class="card-row"><svg width="9" height="11" viewBox="0 0 9 11"><path d="M4.5 0A4 4 0 0 1 8.5 4c0 3-4 7-4 7S.5 7 .5 4a4 4 0 0 1 4-4z" fill="#888"/></svg>Sector-65, Noida</div><div class="card-row"><svg width="10" height="10" viewBox="0 0 10 10"><rect x="1" y="1" width="8" height="9" fill="#888"/></svg>Shopping Complex</div><div class="btn card-btn">View Details</div></div></div>
  <div class="card"><div class="card-img" role="img" aria-label="Shopping complex exterior"></div><div class="card-city">GURGAON</div><div class="card-body"><div class="card-name">Kestrel Cosmopolitan</div><div class="card-row"><svg width="9" height="11" viewBox="0 0 9 11"><path d="M4.5 0A4 4 0 0 1 8.5 4c0 3-4 7-4 7S.5 7 .5 4a4 4 0 0 1 4-4z" fill="#888"/></svg>Sector-65, Noida</div><div class="card-row"><svg width="10" height="10" viewBox="0 0 10 10"><rect x="1" y="1" width="8" height="9" fill="#888"/></svg>Shopping Complex</div><div class="btn card-btn">View Details</div></div></div>
  <div class="card"><div class="card-img" role="img" aria-label="Shopping complex exterior"></div><div class="card-city">GURGAON</div><div class="card-body"><div class="card-name">Kestrel Cosmopolitan</div><div class="card-row"><svg width="9" height="11" viewBox="0 0 9 11"><path d="M4.5 0A4 4 0 0 1 8.5 4c0 3-4 7-4 7S.5 7 .5 4a4 4 0 0 1 4-4z" fill="#888"/></svg>Sector-65, Noida</div><div class="card-row"><svg width="10" height="10" viewBox="0 0 10 10"><rect x="1" y="1" width="8" height="9" fill="#888"/></svg>Shopping Complex</div><div class="btn card-btn">View Details</div></div></div>
</div>

<!-- featured new launches -->
<div class="abs section-head" style="top:1330px"><h2>Featured New Launches</h2><span class="scope">Across India ▾</span><span class="rule"></span></div>

<div class="abs grid" style="top:1398px">
  <div class="card"><div class="card-img" role="img" aria-label="New retail launch building"></div><div class="card-city">GURGAON</div><div class="card-body"><div class="card-name">Kestrel Cosmopolitan</div><div class="card-row"><svg width="9" height="11" viewBox="0 0 9 11"><path d="M4.5 0A4 4 0 0 1 8.5 4c0 3-4 7-4 7S.5 7 .5 4a4 4 0 0 1 4-4z" fill="#888"/></svg>Sector-65, Noida</div><div class="card-row"><svg width="10" height="10" viewBox="0 0 10 10"><rect x="1" y="1" width="8" height="9" fill="#888"/></svg>Shopping Complex</div><div class="btn card-btn">View Details</div></div></div>
  <div class="card"><div class="card-img" role="img" aria-label="New retail launch building"></div><div class="card-city">GURGAON</div><div class="card-body"><div class="card-name">Kestrel Cosmopolitan</div><div class="card-row"><svg width="9" height="11" viewBox="0 0 9 11"><path d="M4.5 0A4 4 0 0 1 8.5 4c0 3-4 7-4 7S.5 7 .5 4a4 4 0 0 1 4-4z" fill="#888"/></svg>Sector-65, Noida</div><div class="card-row"><svg width="10" height="10" viewBox="0 0 10 10"><rect x="1" y="1" width="8" height="9" fill="#888"/></svg>Shopping Complex</div><div class="btn card-btn">View Details</div></div></div>
  <div class="card"><div class="card-img" role="img" aria-label="New retail launch building"></div><div class="card-city">GURGAON</div><div class="card-body"><div class="card-name">Kestrel Cosmopolitan</div><div class="card-row"><svg width="9" height="11" viewBox="0 0 9 11"><path d="M4.5 0A4 4 0 0 1 8.5 4c0 3-4 7-4 7S.5 7 .5 4a4 4 0 0 1 4-4z" fill="#888"/></svg>Sector-65, Noida</div><div class="card-row"><svg width="10" height="10" viewBox="0 0 10 10"><rect x="1" y="1" width="8" height="9" fill="#888"/></svg>Shopping Complex</div><div class="btn card-btn">View Details</div></div></div>
  <div class="card"><div class="card-img" role="img" aria-label="New retail launch building"></div><div class="card-city">GURGAON</div><div class="card-body"><div class="card-name">Kestrel Cosmopolitan</div><div class="card-row"><svg width="9" height="11" viewBox="0 0 9 11"><path d="M4.5 0A4 4 0 0 1 8.5 4c0 3-4 7-4 7S.5 7 .5 4a4 4 0 0 1 4-4z" fill="#888"/></svg>Sector-65, Noida</div><div class="card-row"><svg width="10" height="10" viewBox="0 0 10 10"><rect x="1" y="1" width="8" height="9" fill="#888"/></svg>Shopping Complex</div><div class="btn card-btn">View Details</div></div></div>
  <div class="card"><div class="card-img" role="img" aria-label="New retail launch building"></div><div class="card-city">GURGAON</div><div class="card-body"><div class="card-name">Kestrel Cosmopolitan</div><div class="card-row"><svg width="9" height="11" viewBox="0 0 9 11"><path d="M4.5 0A4 4 0 0 1 8.5 4c0 3-4 7-4 7S.5 7 .5 4a4 4 0 0 1 4-4z" fill="#888"/></svg>Sector-65, Noida</div><div class="card-row"><svg width="10" height="10" viewBox="0 0 10 10"><rect x="1" y="1" width="8" height="9" fill="#888"/></svg>Shopping Complex</div><div class="btn card-btn">View Details</div></div></div>
  <div class="card"><div class="card-img" role="img" aria-label="New retail launch building"></div><div class="card-city">GURGAON</div><div class="card-body"><div class="card-name">Kestrel Cosmopolitan</div><div class="card-row"><svg width="9" height="11" viewBox="0 0 9 11"><path d="M4.5 0A4 4 0 0 1 8.5 4c0 3-4 7-4 7S.5 7 .5 4a4 4 0 0 1 4-4z" fill="#888"/></svg>Sector-65, Noida</div><div class="card-row"><svg width="10" height="10" viewBox="0 0 10 10"><rect x="1" y="1" width="8" height="9" fill="#888"/></svg>Shopping Complex</div><div class="btn card-btn">View Details</div></div></div>
  <div class="card"><div class="card-img" role="img" aria-label="New retail launch building"></div><div class="card-city">GURGAON</div><div class="card-body"><div class="card-name">Kestrel Cosmopolitan</div><div class="card-row"><svg width="9" height="11" viewBox="0 0 9 11"><path d="M4.5 0A4 4 0 0 1 8.5 4c0 3-4 7-4 7S.5 7 .5 4a4 4 0 0 1 4-4z" fill="#888"/></svg>Sector-65, Noida</div><div class="card-row"><svg width="10" height="10" viewBox="0 0 10 10"><rect x="1" y="1" width="8" height="9" fill="#888"/></svg>Shopping Complex</div><div class="btn card-btn">View Details</div></div></div>
  <div class="card"><div class="card-img" role="img" aria-label="New retail launch building"></div><div class="card-city">GURGAON</div><div class="card-body"><div class="card-name">Kestrel Cosmopolitan</div><div class="card-row"><svg width="9" height="11" viewBox="0 0 9 11"><path d="M4.5 0A4 4 0 0 1 8.5 4c0 3-4 7-4 7S.5 7 .5 4a4 4 0 0 1 4-4z" fill="#888"/></svg>Sector-65, Noida</div><div class="card-row"><svg width="10" height="10" viewBox="0 0 10 10"><rect x="1" y="1" width="8" height="9" fill="#888"/></svg>Shopping Complex</div><div class="btn card-btn">View Details</div></div></div>
  <div class="card"><div class="card-img" role="img" aria-label="New retail launch building"></div><div class="card-city">GURGAON</div><div class="card-body"><div class="card-name">Kestrel Cosmopolitan</div><div class="card-row"><svg width="9" height="11" viewBox="0 0 9 11"><path d="M4.5 0A4 4 0 0 1 8.5 4c0 3-4 7-4 7S.5 7 .5 4a4 4 0 0 1 4-4z" fill="#888"/></svg>Sector-65, Noida</div><div class="card-row"><svg width="10" height="10" viewBox="0 0 10 10"><rect x="1" y="1" width="8" height="9" fill="#888"/></svg>Shopping Complex</div><div class="btn card-btn">View Details</div></div></div>
  <div class="card"><div class="card-img" role="img" aria-label="New retail launch building"></div><div class="card-city">GURGAON</div><div class="card-body"><div class="card-name">Kestrel Cosmopolitan</div><div class="card-row"><svg width="9" height="11" viewBox="0 0 9 11"><path d="M4.5 0A4 4 0 0 1 8.5 4c0 3-4 7-4 7S.5 7 .5 4a4 4 0 0 1 4-4z" fill="#888"/></svg>Sector-65, Noida</div><div class="card-row"><svg width="10" height="10" viewBox="0 0 10 10"><rect x="1" y="1" width="8" height="9" fill="#888"/></svg>Shopping Complex</div><div class="btn card-btn">View Details</div></div></div>
</div>

<!-- lot mavens -->
<div class="abs maven"></div>
<div class="abs maven-art" role="img" aria-label="Illustration of a support advisor with headset at a computer"></div>
<div class="abs block-title" style="left:362px;top:1950px">Lot Mavens</div>
<div class="abs block-text" style="left:362px;top:1986px;width:790px">Post your Retail Space requirement with us and our experts shall get back with suitable options and even help you in your transaction. This is a Free Service!</div>
<div class="abs input" style="left:362px;top:2038px;width:311px">✉ Your Email Address</div>
<div class="abs input" style="left:744px;top:2038px;width:308px">☎ Your Contact Number</div>
<div class="abs input textarea" style="left:362px;top:2080px;width:786px;height:88px;padding-top:10px">✎ Description of your requirement</div>
<div class="abs btn" style="left:695px;top:2193px;width:81px;height:23px;line-height:23px;font-size:11px">Send</div>

<!-- editor's choice & listing alert -->
<div class="abs" style="left:0;top:2232px;width:1200px;height:285px;background:var(--panel)"></div>
<div class="abs duo-box" style="left:16px;width:566px"></div>
<div class="abs editors-art" role="img" aria-label="Editor's choice award badge with ribbon"></div>
<div class="abs block-title" style="left:180px;top:2250px">Editor's Choice</div>
<div class="abs block-text" style="left:180px;top:2284px;width:380px;text-align:justify">A "Select" Listing of Retail Properties Handpicked by our Editors based on their own positive evaluation on parameters &amp; attributes such as Design Concept, Location, Developer, Success Potential.<br><br>So Read On &amp; Check Out for yourself!</div>
<div class="abs btn" style="left:452px;top:2440px;width:104px;height:24px;line-height:24px;font-size:11px">Read More</div>

<div class="abs duo-box" style="left:602px;width:578px"></div>
<svg class="abs" style="left:640px;top:2262px" width="110" height="120" viewBox="0 0 110 120"><path d="M55 8c22 0 36 16 36 38v30l12 16H7l12-16V46C19 24 33 8 55 8z" fill="#1f8fe5"/><circle cx="55" cy="106" r="10" fill="#1f8fe5"/><rect x="50" y="0" width="10" height="12" rx="5" fill="#1f8fe5"/></svg>
<div class="abs block-title" style="left:780px;top:2250px">Listing Alert</div>
<div class="abs block-text" style="left:780px;top:2284px;width:380px">Subscribe for Fortnightly Email update on New Listings @ Lotvantage</div>
<div class="abs input" style="left:780px;top:2330px;width:320px">✉ Your Email Address</div>
<div class="abs input" style="left:780px;top:2368px;width:320px;justify-content:space-between">Property Type<span style="color:var(--blue)">▼</span></div>
<div class="abs input" style="left:780px;top:2406px;width:320px;justify-content:space-between">Locality<span style="color:var(--blue)">▼</span></div>
<div class="abs btn" style="left:880px;top:2450px;width:104px;height:24px;line-height:24px;font-size:11px">Subscribe</div>

<!-- footer -->
<div class="abs footer"></div>
<div class="abs brand-light" style="left:26px;top:2552px">
  <div class="brand"><span class="brand-dot"></span><span class="brand-name">Lotvantage</span></div>
  <div class="brand-tag">India's leading portal for retail space</div>
</div>
<div class="abs footer-text">Lotvantage.com is a Specialised Web based platform for Retail Space, featuring properties across India under various formats such as Retail Malls, Shopping Complexes, High-street Shops. Also featured are Retail Warehouses. Hub provide the logistic back-end for the retail business</div>
<div class="abs getintouch">Get in Touch</div>
<div class="abs address"><b style="color:#fff">Storefront Central</b><br>Unit 212, 2nd Floor,<br>Lorem ipsum is simply,<br>Sector 9, Gurgaon - 122011<br><br>Phone : 000-000-0000<br>Fax : 000 - 000 - 0000</div>
<div class="abs social"><i></i><i></i><i></i><i></i><i></i><i></i></div>
<div class="abs input on-dark" style="left:842px;top:2588px;width:306px">👤 Your Name</div>
<div class="abs input on-dark" style="left:842px;top:2630px;width:306px">✉ Your Email Address</div>
<div class="abs input on-dark" style="left:842px;top:2672px;width:306px">☎ Your Contact Number</div>
<div class="abs input textarea on-dark" style="left:842px;top:2711px;width:306px;height:78px;padding-top:8px">Your Message</div>
<div class="abs btn" style="left:968px;top:2802px;width:97px;height:23px;line-height:23px;font-size:11px">Send</div>

<nav class="abs bottom-nav">
  <span>About Us</span><span>Privacy Policy</span><span>Terms of Use</span><span>Contact Us</span><span>Site Map</span><span>Retail Malls</span><span>Shopping Complex</span><span>High Street Shops</span><span>Retail Warehouses</span>
</nav>
<div class="abs copyright">Copyright © 2015 Storefront Central.com, All rights reserved.</div>

</body>
</html>
```